Velmo BUSINESS CARD

Design an attention-grabbing business cards. Draw inspiration from the provided logo file. Please use the same font style as in the logo.
the back side of the card is for accent/decoration.

Contact Information for Business Card

PLEASE USE PROVIDED BUSINESS CARD SAMPLE

Other font styles liked:
• LUMETTE

Colors
EB3D1F
EC4F4E
F09395
F8D3D4
FCEDEE

Requirements
Must have
• RED, BLACK COLORS, SOLID BACK COLOR
Nice to have
• MAKE IT FANCY

```html
<!DOCTYPE html>
<html lang="en">
<head>
<meta charset="utf-8">
<title>Velmo Business Card</title>
<link href="https://fonts.googleapis.com/css2?family=Orbitron:wght@700;900&family=Lato:wght@400&display=swap" rel="stylesheet">
<style>
  :root {
    --stage: #8f8f8f;
    --red: #e0232f;
    --ink: #231f20;
    --black: #070707;
    --white: #ffffff;
  }
  * { margin: 0; padding: 0; box-sizing: border-box; }
  html, body { width: 1047px; height: 1200px; overflow: hidden; }
  body { background: var(--stage); position: relative; font-family: "Lato", sans-serif; }

  .card {
    position: absolute;
    left: 156px;
    width: 743px;
    height: 424px;
    box-shadow: 0 1px 3px rgba(0,0,0,0.35);
    overflow: hidden;
  }
  .card--front { top: 120px; background: var(--red); color: var(--ink); }
  .card--back { top: 634px; background: var(--ink); color: var(--white); }

  .wordmark {
    position: absolute;
    font-family: "Orbitron", sans-serif;
    font-weight: 900;
    line-height: 1;
    white-space: nowrap;
  }
  .card--front .wordmark { left: 37px; top: 39px; font-size: 60px; letter-spacing: 3px; }
  .tagline {
    position: absolute;
    font-family: "Lato", sans-serif;
    letter-spacing: 1px;
    text-transform: uppercase;
    white-space: nowrap;
  }
  .card--front .tagline { left: 38px; top: 101px; font-size: 12px; }

  .person-name {
    position: absolute;
    left: 38px; top: 140px;
    font-family: "Orbitron", sans-serif;
    font-weight: 900;
    font-size: 29px;
    letter-spacing: 2px;
    line-height: 1;
    white-space: nowrap;
  }
  .person-role { position: absolute; left: 38px; top: 173px; font-size: 21px; }

  .contact-list { position: absolute; left: 38px; top: 221px; list-style: none; font-size: 18.5px; line-height: 26px; }
  .contact-item { display: flex; align-items: flex-start; white-space: nowrap; }
  .contact-item--gap { margin-bottom: 7px; }
  .contact-icon { width: 14px; height: 14px; margin: 6px 12px 0 0; flex: none; fill: var(--ink); }

  .brand-square {
    position: absolute;
    left: 369px; top: 44px;
    width: 334px; height: 334px;
    background: var(--ink);
  }

  .back-square {
    position: absolute;
    left: 92px; top: 155px;
    width: 109px; height: 109px;
    background: var(--white);
  }
  .card--back .wordmark { left: 220px; top: 152px; font-size: 95px; letter-spacing: 3px; }
  .card--back .tagline { left: 224px; top: 247px; font-size: 19px; letter-spacing: 2px; color: var(--white); }

  .back-decoration {
    position: absolute;
    right: 0; top: 0;
    width: 420px; height: 100%;
    background: linear-gradient(90deg, rgba(7,7,7,0) 0%, rgba(60,60,60,0.35) 45%, var(--black) 100%);
  }
</style>
</head>
<body>

<section class="card card--front">
  <div class="wordmark">VELMO</div>
  <div class="tagline">Logistics with bite</div>

  <div class="person-name">ROWAN PELL</div>
  <div class="person-role">President</div>

  <ul class="contact-list">
    <li class="contact-item contact-item--gap">
      <svg class="contact-icon" viewBox="0 0 14 14"><path d="M7 0a5 5 0 0 0-5 5c0 3.6 5 9 5 9s5-5.4 5-9a5 5 0 0 0-5-5zm0 7a2 2 0 1 1 0-4 2 2 0 0 1 0 4z"/></svg>
      <span>418 Alder Row<br>Fairhaven, OR, 97120.</span>
    </li>
    <li class="contact-item">
      <svg class="contact-icon" viewBox="0 0 14 14"><path d="M3 0.5l2.2 3-1.3 1.6c.8 1.9 2.2 3.3 4 4.1l1.6-1.3 3 2.2-1.2 2.6C5.6 12.8 1.2 8.4 0.4 2.2z"/></svg>
      <span>555-014-2286</span>
    </li>
    <li class="contact-item">
      <svg class="contact-icon" viewBox="0 0 14 14"><path d="M3.5 0h7v14h-7zM5 2v8h4V2zm2 9.2a.9.9 0 1 0 0 1.8.9.9 0 0 0 0-1.8z"/></svg>
      <span>555-017-3391</span>
    </li>
    <li class="contact-item">
      <svg class="contact-icon" viewBox="0 0 14 14"><path d="M0 3h14v1L7 8 0 4zM0 5.5l7 4 7-4V11H0z"/></svg>
      <span>RPell@velmo-llc.com</span>
    </li>
    <li class="contact-item">
      <svg class="contact-icon" viewBox="0 0 14 14"><path d="M7 0a7 7 0 1 0 0 14A7 7 0 0 0 7 0zm4.8 6H9.9a10 10 0 0 0-1-4.3A5.1 5.1 0 0 1 11.8 6zM7 1.9c.6.8 1.1 2.3 1.2 4.1H5.8C5.9 4.2 6.4 2.7 7 1.9zM5.1 1.7A10 10 0 0 0 4.1 6H2.2a5.1 5.1 0 0 1 2.9-4.3zM2.2 8h1.9c.1 1.6.5 3.1 1 4.3A5.1 5.1 0 0 1 2.2 8zM7 12.1c-.6-.8-1.1-2.3-1.2-4.1h2.4c-.1 1.8-.6 3.3-1.2 4.1zm1.9.2c.5-1.2.9-2.7 1-4.3h1.9a5.1 5.1 0 0 1-2.9 4.3z"/></svg>
      <span>www.Velmo-LLC.com</span>
    </li>
  </ul>

  <div class="brand-square"></div>
</section>

<section class="card card--back">
  <div class="back-decoration" role="img" aria-label="Faint large brand emblem decoration fading into black"></div>
  <div class="back-square"></div>
  <div class="wordmark">VELMO</div>
  <div class="tagline">Logistics with bite</div>
</section>

</body>
</html>
```